Criação de Layout de Post para Alimentos & Bebidas
A empresa queria:
" Restaurante com petiscos, a la carte, bebidas. Funcionamos a partir de 8hs da manhã, de segunda a quinta até as 23h e finais de semana até as 2h da manhã "

```html
<!DOCTYPE html>
<html lang="pt-BR">
<head>
<meta charset="UTF-8">
<title>Brasada – Feliz 2019</title>
<link rel="stylesheet" href="https://fonts.googleapis.com/css2?family=Lato:wght@400;700;900&family=Kaushan+Script&display=swap">
<style>
  :root {
    --gold-dark: #b58c52;
    --gold-mid: #d6b47e;
    --gold-light: #ecd3a4;
    --ink: #1d1a18;
    --night: #120d0a;
    --night-warm: #2a1a10;
    --spark: #e08a2c;
    --white: #ffffff;
  }
  * { margin: 0; padding: 0; box-sizing: border-box; }
  html, body { width: 1200px; height: 1200px; overflow: hidden; background: var(--night); }
  .post {
    position: relative;
    width: 1200px;
    height: 1200px;
    overflow: hidden;
    font-family: "Lato", Arial, sans-serif;
  }
  .brand-panel {
    position: absolute;
    left: 0; top: 0;
    width: 476px; height: 1200px;
    background: linear-gradient(100deg,
      var(--gold-dark) 0%,
      var(--gold-mid) 22%,
      var(--gold-light) 45%,
      var(--gold-mid) 62%,
      var(--gold-dark) 82%,
      var(--gold-mid) 100%);
  }
  .brand {
    position: absolute;
    left: 0; top: 88px;
    width: 476px;
    text-align: center;
    color: var(--ink);
  }
  .brand-mark {
    display: block;
    width: 132px; height: 132px;
    margin: 0 auto 22px;
    border-radius: 50%;
    background: var(--ink);
  }
  .brand-name {
    font-weight: 900;
    font-size: 74px;
    line-height: 1;
    letter-spacing: 1px;
  }
  .brand-tagline {
    margin-top: 10px;
    font-weight: 700;
    font-size: 25px;
    letter-spacing: 2px;
  }
  .contacts {
    position: absolute;
    left: 50px; top: 868px;
    list-style: none;
    color: var(--ink);
  }
  .contact {
    display: flex;
    align-items: center;
    height: 56px;
    margin-bottom: 38px;
    font-size: 37px;
  }
  .contact-icon {
    width: 50px; height: 50px;
    margin-right: 26px;
    flex: none;
  }
  .celebration {
    position: absolute;
    left: 476px; top: 0;
    width: 724px; height: 1200px;
    background:
      radial-gradient(circle at 30% 20%, rgba(224,138,44,0.45) 0, transparent 22%),
      radial-gradient(circle at 85% 12%, rgba(224,138,44,0.35) 0, transparent 18%),
      radial-gradient(circle at 70% 55%, rgba(224,138,44,0.25) 0, transparent 25%),
      radial-gradient(circle at 20% 85%, rgba(224,138,44,0.3) 0, transparent 20%),
      radial-gradient(circle at 90% 88%, rgba(224,138,44,0.3) 0, transparent 18%),
      linear-gradient(160deg, var(--night-warm) 0%, var(--night) 55%, var(--night-warm) 100%);
  }
  .greeting {
    position: absolute;
    left: 476px; top: 370px;
    width: 724px;
    text-align: center;
    color: var(--white);
    font-family: "Kaushan Script", cursive;
    line-height: 1;
  }
  .greeting-word { font-size: 240px; }
  .greeting-year { font-size: 240px; margin-top: 20px; }
</style>
</head>
<body>
<main class="post">
  <section class="brand-panel">
    <div class="brand">
      <span class="brand-mark"></span>
      <div class="brand-name">Brasada</div>
      <div class="brand-tagline">BAR E RESTAURANTE</div>
    </div>
    <ul class="contacts">
      <li class="contact">
        <svg class="contact-icon" viewBox="0 0 50 50"><circle cx="25" cy="25" r="21" fill="none" stroke="var(--ink)" stroke-width="4"/></svg>
        <span>/brasadabar</span>
      </li>
      <li class="contact">
        <svg class="contact-icon" viewBox="0 0 50 50"><circle cx="25" cy="25" r="21" fill="none" stroke="var(--ink)" stroke-width="4"/></svg>
        <span>@brasadabar</span>
      </li>
      <li class="contact">
        <svg class="contact-icon" viewBox="0 0 50 50"><path d="M15 8 L22 8 L25 17 L20 21 C23 28 26 31 31 34 L35 29 L44 32 L44 39 C44 42 41 44 38 44 C22 42 8 28 7 13 C7 10 10 8 15 8 Z" fill="var(--ink)"/></svg>
        <span>(00) 22222 3333</span>
      </li>
    </ul>
  </section>
  <div class="celebration" role="img" aria-label="Fotografia de fogos de artifício com brilhos dourados e laranja sobre céu noturno"></div>
  <h1 class="greeting">
    <div class="greeting-word">Feliz</div>
    <div class="greeting-year">2019</div>
  </h1>
</main>
</body>
</html>
```